Modern and Improved business card design for Family Dental Practice

We have 2 sets of logo we have designed and now just need a business card layout and design for the office. Colors are on the logo. We can choose which logo we want to go with . The font can be changed to whatever seems modern and relevant. We are family dental office that has been open for over 15 years in South Austin Texas.

Target Market(s)

Handout Business cards to referrals and specialists

Industry/Entity Type

Dental

Contact Information for Business Card

We need address, phone, website and email address. 4830 North Maple Loop Suite 208 , Austin,Texas 78392....phone: 512-847-3195.....email- info@bluepinedental.example....website - BluePineDental.example

Font styles to use
Serif
Decorative

Requirements
Must have
• my logo. We have 2 logos, but we can use just one or if we can incorporate one on one side and the other on the other side.
Nice to have
• Really just need a modern look and clean that incorporates the logo and colors .

```html
<!DOCTYPE html>
<html lang="en">
<head>
<meta charset="utf-8">
<title>Blue Pine Family Dentistry – Business Card</title>
<link rel="stylesheet" href="https://fonts.googleapis.com/css2?family=Noto+Serif:ital,wght@0,400;1,400&display=swap">
<style>
  :root {
    --backdrop: #8f8f8f;
    --card: #ffffff;
    --green: #1f6b12;
    --rule: #c9cfc4;
    --ink: #333333;
    --muted: #555555;
  }
  * { box-sizing: border-box; margin: 0; padding: 0; }
  html, body { width: 1200px; height: 1200px; overflow: hidden; }
  body {
    background: var(--backdrop);
    font-family: "Noto Serif", Georgia, serif;
    position: relative;
  }
  .card {
    position: absolute;
    left: 281px;
    width: 638px;
    height: 366px;
    background: var(--card);
    border-radius: 22px;
    overflow: hidden;
  }
  .card-front { top: 195px; }
  .card-back { top: 639px; }

  /* Front */
  .brand {
    position: absolute;
    left: 70px;
    top: 138px;
    display: flex;
    align-items: center;
    gap: 12px;
  }
  .brand-dot {
    width: 40px; height: 40px;
    border-radius: 50%;
    background: var(--green);
    flex: none;
  }
  .brand-name {
    color: var(--green);
    font-size: 19px;
    line-height: 1.25;
    font-weight: 400;
    width: 150px;
  }
  .divider {
    position: absolute;
    left: 302px;
    top: 72px;
    width: 1px;
    height: 218px;
    background: var(--rule);
  }

  .contact { position: absolute; left: 348px; top: 80px; }
  .person-name {
    font-size: 27px;
    font-weight: 400;
    color: var(--ink);
    letter-spacing: 1px;
    line-height: 1.1;
  }
  .person-title {
    font-size: 16px;
    color: var(--green);
    margin-top: 2px;
  }
  .address {
    margin-top: 12px;
    font-size: 15px;
    color: var(--ink);
    line-height: 20px;
    letter-spacing: 0.4px;
  }
  .channels { list-style: none; margin-top: 14px; }
  .channels li {
    display: flex;
    align-items: center;
    gap: 8px;
    font-size: 15px;
    color: var(--ink);
    line-height: 20px;
    letter-spacing: 0.3px;
  }
  .channels svg { width: 14px; height: 14px; flex: none; }

  /* Back */
  .appt-heading {
    position: absolute;
    top: 38px; left: 0; right: 0;
    text-align: center;
    color: var(--green);
    font-size: 26px;
    font-weight: 400;
    letter-spacing: 1.5px;
  }
  .field-row {
    position: absolute;
    left: 56px;
    width: 528px;
    display: flex;
    align-items: baseline;
    color: var(--green);
    font-size: 14px;
  }
  .field-row.name-row { top: 115px; }
  .field-row.date-row { top: 165px; }
  .fill {
    flex: 1;
    border-bottom: 1.5px dotted var(--green);
    margin: 0 1px;
    transform: translateY(-3px);
  }
  .fill.date { flex: 1.35; }
  .suffix { font-size: 11px; }

  .days {
    position: absolute;
    top: 228px; left: 0;
    width: 100%;
    height: 22px;
    list-style: none;
    font-size: 15px;
    color: var(--muted);
  }
  .days li { position: absolute; top: 0; display: flex; align-items: center; gap: 3px; }
  .day-mon { left: 81px; }
  .day-tue { left: 171px; }
  .day-wed { left: 264px; }
  .day-thu { left: 351px; }
  .day-fri { left: 438px; }
  .day-sat { left: 514px; }
  .tick-box {
    width: 12px; height: 12px;
    border: 2px solid var(--green);
  }
  .policy {
    position: absolute;
    top: 297px; left: 0; right: 0;
    text-align: center;
    font-style: italic;
    font-size: 11.5px;
    line-height: 14px;
    color: var(--muted);
    letter-spacing: 0.3px;
  }
</style>
</head>
<body>

<section class="card card-front" aria-label="Business card front">
  <div class="brand">
    <span class="brand-dot"></span>
    <span class="brand-name">Blue Pine Family Dentistry</span>
  </div>

  <span class="divider" aria-hidden="true"></span>

  <div class="contact">
    <h1 class="person-name">YOUR NAME</h1>
    <p class="person-title">Dr Your Title</p>
    <p class="address">4830 North Maple Loop<br>Suite 208<br>Austin,Texas 78392</p>
    <ul class="channels">
      <li>
        <svg viewBox="0 0 16 16" aria-hidden="true"><path d="M3 1.5l2.5 0 1 3.5-1.6 1.2a8 8 0 0 0 4.9 4.9L11 9.5l3.5 1v2.5c0 .8-.7 1.5-1.5 1.5C7 14.5 1.5 9 1.5 3c0-.8.7-1.5 1.5-1.5z" fill="var(--green)"/></svg>
        512-847-3195
      </li>
      <li>
        <svg viewBox="0 0 16 16" aria-hidden="true"><rect x="1" y="3" width="14" height="10" fill="var(--green)"/><path d="M1 3l7 5.5L15 3" fill="none" stroke="#fff" stroke-width="1.3"/></svg>
        info@bluepinedental.example
      </li>
      <li>
        <svg viewBox="0 0 16 16" aria-hidden="true"><circle cx="8" cy="8" r="7" fill="var(--green)"/><path d="M1 8h14M8 1c-3 3-3 11 0 14M8 1c3 3 3 11 0 14" fill="none" stroke="#fff" stroke-width="1"/></svg>
        BluePineDental.example
      </li>
    </ul>
  </div>
</section>

<section class="card card-back" aria-label="Business card back">
  <h2 class="appt-heading">NEXT APPOINTMENT</h2>

  <div class="field-row name-row">
    <span>NAME</span><span class="fill"></span>
  </div>
  <div class="field-row date-row">
    <span>DATE</span><span class="fill date"></span>
    <span>TIME</span><span class="fill"></span>
    <span class="suffix">AM\PM</span>
  </div>

  <ul class="days">
    <li class="day-mon"><span class="tick-box"></span>MON</li>
    <li class="day-tue"><span class="tick-box"></span>TUES</li>
    <li class="day-wed"><span class="tick-box"></span>WED</li>
    <li class="day-thu"><span class="tick-box"></span>THU</li>
    <li class="day-fri"><span class="tick-box"></span>FRI</li>
    <li class="day-sat"><span class="tick-box"></span>SAT</li>
  </ul>

  <p class="policy">If you are unable to keep your appointment, please call us to<br>reschedule at least 48 hours prior to your appointment.</p>
</section>

</body>
</html>
```